Quorvane Capital Modern Business Card

We need a modern business card template designed for Quorvane Capital.
Quorvane Capital is a diversified global cryptocurrency investment fund.

The font under the logo: Hiragino Kaku Gothic Pro

Color Hexcode: Main colors white (ffffff) & teal (188383), we are open to adding #fcca46 as an accent

Target Market(s)

Accredited Investors, high net worth individuals and institutional investors

Industry/Entity Type

Investment

Contact Information for Business Card

Contact Information should contain
Name
main phone +1 720 555 0147
cell
email

Font styles to use
Sans Serif
Other font styles liked:
• Hiragino Kaku Gothic Pro

Requirements
Must have
• would like to have icons that identify the contact information
• include our website: www.quorvanecapital.example
• include our Tagline: Diversified Crypto Investment Funds
Nice to have
• Would like to have a simple back side with the logo (without the words) and plenty of space

```html
<!DOCTYPE html>
<html lang="en">
<head>
<meta charset="utf-8">
<title>Quorvane Capital Business Card</title>
<link rel="stylesheet" href="https://fonts.googleapis.com/css2?family=Open+Sans:wght@400;600;700&display=swap">
<style>
  :root {
    --teal: #21969a;
    --teal-dark: #188383;
    --white: #ffffff;
    --ink: #1b1b1b;
    --ink-soft: #333333;
    --watermark: #eef3f4;
    --backdrop: #e7e4e0;
  }
  * { box-sizing: border-box; margin: 0; padding: 0; }
  html, body {
    width: 1200px; height: 1200px; overflow: hidden;
    background: var(--backdrop);
    font-family: "Open Sans", Arial, sans-serif;
  }
  .canvas { position: relative; width: 1200px; height: 1200px; }
  .card {
    position: absolute; left: 180px; width: 840px; height: 480px;
    overflow: hidden;
    box-shadow: 0 6px 18px rgba(0,0,0,0.12);
  }
  /* Back side */
  .card-back { top: 70px; background: var(--teal); display: flex; align-items: center; justify-content: center; }
  .card-back .brand-name {
    color: var(--white); font-weight: 600; font-size: 40px; letter-spacing: 4px; text-transform: uppercase;
  }
  /* Front side */
  .card-front { top: 640px; background: var(--white); }
  .front-brand {
    position: absolute; top: 44px; right: 56px;
    display: flex; align-items: center; gap: 12px;
  }
  .front-brand .mark-square { width: 18px; height: 18px; background: var(--teal); }
  .front-brand .brand-name {
    color: var(--teal); font-weight: 600; font-size: 20px; letter-spacing: 1.5px; text-transform: uppercase;
  }
  .watermark-name {
    position: absolute; top: 100px; right: 60px;
    color: var(--watermark); font-weight: 700; font-size: 62px; letter-spacing: 6px; text-transform: uppercase;
    white-space: nowrap; line-height: 1;
  }
  .holder { position: absolute; left: 60px; top: 190px; }
  .holder-name { font-weight: 700; font-size: 40px; color: var(--ink); letter-spacing: 0.5px; line-height: 1; text-transform: uppercase; }
  .holder-title { font-size: 22px; color: var(--ink-soft); margin-top: 4px; }
  .contact-list { position: absolute; left: 64px; top: 276px; list-style: none; }
  .contact-item { display: flex; align-items: center; gap: 14px; height: 32px; font-size: 20px; color: var(--ink-soft); }
  .contact-item svg { width: 20px; height: 20px; flex: none; }
  .contact-label { color: var(--teal); font-weight: 600; }
  .corner-band { position: absolute; left: 40px; bottom: 0; width: 110px; height: 34px; background: var(--teal); }
  .tagline {
    position: absolute; right: 40px; bottom: 18px;
    font-size: 22px; letter-spacing: 1px; color: var(--ink-soft);
  }
</style>
</head>
<body>
<main class="canvas">
  <section class="card card-back" aria-label="Card back">
    <span class="brand-name">Quorvane Capital</span>
  </section>

  <section class="card card-front" aria-label="Card front">
    <div class="front-brand">
      <span class="mark-square"></span>
      <span class="brand-name">Quorvane Capital</span>
    </div>
    <div class="watermark-name" aria-hidden="true">Quorvane</div>

    <div class="holder">
      <p class="holder-name">Dana Whitlow</p>
      <p class="holder-title">Manager</p>
    </div>

    <ul class="contact-list">
      <li class="contact-item">
        <svg viewBox="0 0 20 20" aria-hidden="true"><path fill="var(--teal)" d="M4 2h3l1.5 4-2 1.3a10 10 0 0 0 6.2 6.2L14 11.5l4 1.5v3a2 2 0 0 1-2 2A14 14 0 0 1 2 4a2 2 0 0 1 2-2z"/></svg>
        <span>+1 720 555 0147</span>
      </li>
      <li class="contact-item">
        <svg viewBox="0 0 20 20" aria-hidden="true"><rect x="5" y="1" width="10" height="18" rx="2" fill="var(--teal)"/><rect x="7" y="3.5" width="6" height="11" fill="var(--white)"/><circle cx="10" cy="16.8" r="1" fill="var(--white)"/></svg>
        <span><span class="contact-label">Cell</span> +1 720 555 0193</span>
      </li>
      <li class="contact-item">
        <svg viewBox="0 0 20 20" aria-hidden="true"><rect x="1" y="4" width="18" height="12" fill="var(--teal)"/><path d="M1.5 4.5 10 11l8.5-6.5" fill="none" stroke="var(--white)" stroke-width="1.5"/></svg>
        <span>yourmail@example.com</span>
      </li>
      <li class="contact-item">
        <svg viewBox="0 0 20 20" aria-hidden="true"><circle cx="10" cy="10" r="8.5" fill="var(--teal)"/><path d="M1.5 10h17M10 1.5c-3 3-3 14 0 17M10 1.5c3 3 3 14 0 17" fill="none" stroke="var(--white)" stroke-width="1.2"/></svg>
        <span>www.quorvanecapital.example</span>
      </li>
    </ul>

    <div class="corner-band"></div>
    <p class="tagline">Diversified Crypto Investment Funds</p>
  </section>
</main>
</body>
</html>
```